Vitamin B12 Liquid Drops Label

hi, i need a label designed for my vitamin b12 drops that i am going to be selling on bazaroo. the label needs to quickly capture the attention of a buyer as he or she is scrolling through the thumbnail search results on bazaroo.example my brand is called zulpa. i already have an example brand logo i will be using, however, i need help designing the rest of the label. attached are some examples of labels i like for other supplements.some of these examples are pink. i do not want pink. please go for a blue/green color scheme. THE DESIGN MUST BE BOLD

Target Market(s)

adults ages 30 - 64

Font styles to use
Sans Serif

Colors
0455a3
cedeed
3176b5
85acd3
cfdeed
9bcb3b
abd037
cadf82
00a990

Requirements
Must have
• - bold design
• - somewhat gender-neutral color scheme because this will be used equally by men and women
• - B12 MUST be very prominent and visible on the label
Should not have
• - it should not be "crunchy" looking

```html
<!DOCTYPE html>
<html lang="en">
<head>
<meta charset="utf-8">
<title>Zulpa B-12 Label</title>
<link href="https://fonts.googleapis.com/css2?family=Archivo+Black&family=Heebo:wght@900&family=Roboto+Condensed:wght@400;700&family=Montserrat:wght@700&display=swap" rel="stylesheet">
<style>
  :root {
    --page-bg: #e6e7e9;
    --label-navy: #1f2f6e;
    --label-deep: #141c4a;
    --label-mid: #24418c;
    --brand-blue: #0455a3;
    --brand-teal: #00a990;
    --brand-green: #9bcb3b;
    --brand-lime: #cadf82;
    --text-white: #ffffff;
    --rule-soft: rgba(255,255,255,0.55);
  }
  * { margin: 0; padding: 0; box-sizing: border-box; }
  html, body { width: 790px; height: 1200px; overflow: hidden; }
  body { background: var(--page-bg); position: relative; }

  .label {
    position: absolute;
    left: 65px; top: 105px;
    width: 660px; height: 990px;
    overflow: hidden;
    background: radial-gradient(ellipse 80% 45% at 50% 40%, var(--label-mid) 0%, var(--label-navy) 55%, var(--label-deep) 100%);
  }
  .label__art { position: absolute; inset: 0; width: 100%; height: 100%; }

  .brand {
    position: absolute;
    left: 12px; right: 12px; top: 32px; height: 130px;
    border: 3px solid var(--text-white);
    border-radius: 8px;
    background: rgba(10, 16, 50, 0.6);
    display: flex; align-items: center; justify-content: center;
  }
  .brand__name {
    font-family: "Archivo Black", sans-serif;
    font-size: 118px;
    line-height: 1;
    color: var(--text-white);
    letter-spacing: 2px;
  }

  .product {
    position: absolute;
    left: 0; right: 0; top: 318px;
    text-align: center;
    font-family: "Heebo", sans-serif;
    font-weight: 900;
    font-size: 215px;
    line-height: 1;
    color: var(--text-white);
    letter-spacing: -2px;
  }

  .tagline {
    position: absolute;
    left: 86px; right: 86px; top: 532px; height: 64px;
    border: 1.5px solid var(--rule-soft);
    border-radius: 14px;
    display: flex; align-items: center; justify-content: center;
    font-family: "Roboto Condensed", sans-serif;
    font-weight: 400;
    font-size: 50px;
    color: var(--text-white);
  }

  .supplement {
    position: absolute;
    left: 20px; top: 920px;
    font-family: "Montserrat", sans-serif;
    font-weight: 700;
    font-size: 20px;
    color: var(--text-white);
  }

  .volume {
    position: absolute;
    right: 10px; top: 830px;
    width: 118px; height: 140px;
    border-radius: 14px;
    background: var(--label-navy);
    border: 2px solid var(--brand-green);
    display: flex; flex-direction: column; align-items: center; justify-content: center;
    font-family: "Roboto Condensed", sans-serif;
    font-weight: 700;
    font-size: 42px;
    line-height: 1.2;
    color: var(--text-white);
  }
</style>
</head>
<body>
  <div class="label">
    <svg class="label__art" viewBox="0 0 660 990" preserveAspectRatio="none" aria-hidden="true">
      <defs>
        <radialGradient id="horizonGlow" cx="50%" cy="50%" r="50%">
          <stop offset="0" stop-color="#ffffff" stop-opacity="0.95"/>
          <stop offset="0.25" stop-color="#6cc8ff" stop-opacity="0.7"/>
          <stop offset="1" stop-color="#1f2f6e" stop-opacity="0"/>
        </radialGradient>
        <linearGradient id="waveFill" x1="0" y1="1" x2="1" y2="0">
          <stop offset="0" stop-color="#0455a3"/>
          <stop offset="0.55" stop-color="#00a990"/>
          <stop offset="1" stop-color="#9bcb3b"/>
        </linearGradient>
      </defs>
      <ellipse cx="330" cy="198" rx="330" ry="55" fill="url(#horizonGlow)"/>
      <rect x="0" y="195" width="660" height="3" fill="#bfe8ff" opacity="0.8"/>
      <path d="M0 840 C160 900 330 830 470 720 C560 650 620 620 660 610 L660 990 L0 990 Z" fill="url(#waveFill)"/>
      <path d="M0 870 C170 930 360 860 500 760 C580 700 630 680 660 675 L660 990 L0 990 Z" fill="#1c3a8c"/>
      <path d="M0 835 C160 880 330 820 470 720" fill="none" stroke="#cadf82" stroke-width="2" opacity="0.85"/>
      <path d="M0 800 C120 820 230 860 300 850" fill="none" stroke="#cadf82" stroke-width="1.5" opacity="0.7"/>
      <path d="M20 780 C140 800 250 840 330 840" fill="none" stroke="#85acd3" stroke-width="1.5" opacity="0.6"/>
    </svg>

    <div class="brand"><span class="brand__name">ZULPA</span></div>
    <div class="product">B-12</div>
    <div class="tagline">FAST ACTING COMPLEX</div>
    <div class="supplement">DIETARY SUPPLEMENT</div>
    <div class="volume"><span>2</span><span>FL OZ</span></div>
  </div>
</body>
</html>
```